Stationary mockup / corporate identity stationary presentation

We have developed a business card, envelope, and so on. We want to use a stationary mock up for internal presentation using a mock up template. The idea behind the logo is OK, we do not want to change, but we want to look for some creativity, we have a business card, letter head stationary, complements card, evenloppe etc. For mock up example templates, please look at: https://plovermarks.com/free-kit-layout-sheet-psd-samples/ We include the logo as word document. There are two logo's similar but differnet colors and name. These represent two activities within the same group company. For both we want to have a presentation and be stationary mock up. What we need is a complete presentation of different corporate identity items as a business card, envelope, letterhead stationary, compliments cards, pen, muck, etc. etc. mock up or please check: https: // plovermarks. com / free-kit-layout-sheet-psd-samples / http://www.quillbarrow.com/index.php?site=forum_topic&topic=1 Please look at website: http://www.dunwelloprey.com/varsik/ This is sister website. For LUMBINO will be the same.

Industry/Entity Type

Architecture

Font styles to use
Sans Serif

Colors
33a6d7

Requirements
Must have
• Please look at website: http://www.dunwelloprey.com/varsik/ This is sister website. For LUMBINO will be the same. How if you want. We want to search for uniformity in website and stationary design. But are open for suggestions offcourse.
Nice to have

```html
<!DOCTYPE html>
<html lang="en">
<head>
<meta charset="utf-8">
<title>Lumbino stationery set</title>
<link href="https://fonts.googleapis.com/css2?family=Roboto:wght@300;400&display=swap" rel="stylesheet">
<style>
  :root {
    --backdrop: #1f1f1f;
    --brand-blue: #33a6d7;
    --dot-blue: #3a8ad8;
    --paper: #ebebeb;
    --paper-back: #d6d6d6;
    --ink: #1c1c1c;
    --muted: #7a7a7a;
    --band: #2b2b2b;
    --white: #ffffff;
    --pen-dark: #121212;
    --pen-light: #3a3a3a;
  }
  * { box-sizing: border-box; margin: 0; padding: 0; }
  html, body { width: 1200px; height: 1200px; overflow: hidden; }
  body {
    background: var(--backdrop);
    font-family: "Roboto", Arial, sans-serif;
    position: relative;
  }
  .piece { position: absolute; }

  .brand { display: flex; align-items: center; color: var(--ink); font-weight: 300; line-height: 1; }
  .brand-dot { border-radius: 50%; background: var(--dot-blue); flex: none; }
  .on-blue .brand-dot { background: var(--white); }

  /* Letterheads */
  .letterhead {
    width: 440px; height: 622px;
    background: var(--paper);
    padding: 56px 48px;
  }
  .letterhead.back { left: 40px; top: 150px; background: var(--paper-back); }
  .letterhead.front { left: 80px; top: 200px; }
  .letterhead .brand { font-size: 22px; gap: 10px; }
  .letterhead .brand-dot { width: 12px; height: 12px; }
  .letterhead-footer {
    position: absolute; left: 48px; right: 48px; bottom: 40px;
    border-top: 1px solid var(--muted);
    padding-top: 8px;
    display: flex; justify-content: space-between; align-items: flex-end;
    font-size: 9px; color: var(--muted); line-height: 1.5;
  }
  .letterhead-footer .web { text-align: right; }

  /* Pen */
  .pen {
    left: 200px; top: 880px; width: 240px; height: 16px;
    border-radius: 8px;
    background: linear-gradient(180deg, var(--pen-light), var(--pen-dark));
  }

  /* Notebook */
  .notebook {
    left: 600px; top: 90px; width: 300px; height: 420px;
    background: var(--brand-blue);
    border-radius: 4px 10px 10px 4px;
  }
  .notebook-band {
    position: absolute; top: 0; bottom: 0; right: 34px; width: 12px;
    background: var(--band);
  }
  .notebook .brand { position: absolute; left: 30px; bottom: 36px; font-size: 21px; gap: 10px; }
  .notebook .brand-dot { width: 12px; height: 12px; }

  /* Envelope */
  .envelope { left: 570px; top: 560px; width: 580px; height: 330px; }
  .envelope svg { position: absolute; inset: 0; }
  .envelope .brand { position: absolute; left: 34px; bottom: 38px; font-size: 30px; gap: 14px; }
  .envelope .brand-dot { width: 16px; height: 16px; }

  /* Business cards */
  .card { width: 255px; height: 150px; top: 930px; }
  .card.front { left: 570px; background: var(--brand-blue); }
  .card.front .brand { position: absolute; left: 30px; bottom: 42px; font-size: 16px; gap: 8px; }
  .card.front .brand-dot { width: 9px; height: 9px; }
  .card.back { left: 860px; background: var(--white); padding: 34px 30px; }
  .card.back .brand { font-size: 13px; gap: 7px; }
  .card.back .brand-dot { width: 8px; height: 8px; }
  .card-contact { margin-top: 12px; font-size: 8px; color: var(--muted); line-height: 1.6; }
</style>
</head>
<body>

  <section class="piece letterhead back" aria-label="Letterhead, second sheet">
    <div class="brand"><span class="brand-dot"></span>lumbino</div>
    <div class="letterhead-footer">
      <span>+33 (0) 412 500 318</span>
      <span class="web">contact@lumbino-atelier.com<br>http://www.lumbino-atelier.com</span>
    </div>
  </section>

  <section class="piece letterhead front" aria-label="Letterhead">
    <div class="brand"><span class="brand-dot"></span>lumbino</div>
    <div class="letterhead-footer">
      <span>+33 (0) 412 500 318</span>
      <span class="web">contact@lumbino-atelier.com<br>http://www.lumbino-atelier.com</span>
    </div>
  </section>

  <div class="piece pen" role="img" aria-label="Black fountain pen with gold trim"></div>

  <section class="piece notebook on-blue" aria-label="Notebook cover">
    <div class="notebook-band"></div>
    <div class="brand"><span class="brand-dot"></span>lumbino</div>
  </section>

  <section class="piece envelope on-blue" aria-label="Envelope">
    <svg width="580" height="330" viewBox="0 0 580 330">
      <rect x="0" y="60" width="580" height="270" fill="var(--brand-blue)"/>
      <polygon points="0,60 40,0 540,0 580,60" fill="var(--band)"/>
    </svg>
    <div class="brand"><span class="brand-dot"></span>lumbino</div>
  </section>

  <section class="piece card front on-blue" aria-label="Business card, front">
    <div class="brand"><span class="brand-dot"></span>lumbino</div>
  </section>

  <section class="piece card back" aria-label="Business card, back">
    <div class="brand"><span class="brand-dot"></span>lumbino</div>
    <p class="card-contact">http://www.lumbino-atelier.com<br>contact@lumbino-atelier.com<br>+33 (0) 412 500 318</p>
  </section>

</body>
</html>
```